Road Construction Company needs business cards

We would like a new business card designed for our business.

We're a road construction company based in Qld, Australia.

Can the business card please have the following information on it.

Name: Brent Malvoy
Position: General Manager
Phone: 0471 592 304
Email: Brent.malvoy@quendix.com.au
Address: 87 Harrowgate Ave, Pindarra, QLD, 4000
Website: www.quendix.com.au

Visually we'd like the card to be professional and simple.

Attached is our logo.

Our website is www.quendix.com.au

Target Market(s)

Men aged 25-60

Contact Information for Business Card

As listed in project description

Font styles to use
Serif

Requirements
Must have
• Large logo on back of card

```html
<!DOCTYPE html>
<html lang="en">
<head>
<meta charset="utf-8">
<title>Quendix Business Card</title>
<link href="https://fonts.googleapis.com/css2?family=Montserrat:wght@400;500;800&display=swap" rel="stylesheet">
<style>
  :root {
    --brand-blue: #0752a0;
    --accent-blue: #2aa3dc;
    --text-grey: #444444;
    --backdrop: #9c9c9c;
    --paper: #ffffff;
  }
  * { margin: 0; padding: 0; box-sizing: border-box; }
  html, body {
    width: 1021px;
    height: 1200px;
    overflow: hidden;
    background: var(--backdrop);
    font-family: "Montserrat", Arial, sans-serif;
  }
  .card {
    position: absolute;
    left: 138px;
    width: 745px;
    height: 426px;
    overflow: hidden;
  }
  .card-front {
    top: 121px;
    background: var(--brand-blue);
    display: flex;
    align-items: center;
    justify-content: center;
  }
  .front-wordmark {
    color: var(--paper);
    font-weight: 800;
    font-size: 66px;
    letter-spacing: 2px;
    margin-top: -20px;
  }
  .card-back {
    top: 651px;
    background: var(--paper);
  }
  .back-wordmark {
    position: absolute;
    right: 35px;
    top: 36px;
    color: var(--brand-blue);
    font-weight: 800;
    font-size: 42px;
    letter-spacing: 1px;
    line-height: 1;
  }
  .person-name {
    position: absolute;
    left: 35px;
    top: 198px;
    color: var(--brand-blue);
    font-weight: 800;
    font-size: 27px;
    line-height: 1.1;
  }
  .person-title {
    position: absolute;
    left: 35px;
    top: 231px;
    color: var(--accent-blue);
    font-weight: 500;
    font-size: 19px;
  }
  .divider {
    position: absolute;
    left: 35px;
    right: 35px;
    top: 275px;
    height: 2px;
    background: var(--brand-blue);
  }
  .contact-list {
    position: absolute;
    left: 35px;
    top: 302px;
    list-style: none;
    color: var(--text-grey);
    font-size: 19px;
    line-height: 28px;
  }
  .contact-list li { display: flex; align-items: center; gap: 7px; }
  .contact-list svg { width: 18px; height: 18px; fill: var(--brand-blue); }
  .address {
    position: absolute;
    right: 35px;
    top: 302px;
    text-align: right;
    font-style: normal;
    color: var(--text-grey);
    font-size: 19px;
    line-height: 28px;
  }
  .footer-bands {
    position: absolute;
    left: 0;
    bottom: 0;
    width: 745px;
    height: 50px;
  }
  .website {
    position: absolute;
    right: 35px;
    bottom: 17px;
    color: var(--paper);
    font-size: 18px;
    font-weight: 500;
  }
</style>
</head>
<body>
  <section class="card card-front">
    <div class="front-wordmark">QUENDIX</div>
  </section>

  <section class="card card-back">
    <div class="back-wordmark">QUENDIX</div>

    <h1 class="person-name">BRENT MALVOY</h1>
    <p class="person-title">General Manager</p>
    <div class="divider"></div>

    <ul class="contact-list">
      <li>
        <svg viewBox="0 0 24 24" aria-hidden="true"><path d="M6.6 10.8a15.2 15.2 0 0 0 6.6 6.6l2.2-2.2c.3-.3.7-.4 1-.2 1.1.4 2.3.6 3.6.6.6 0 1 .4 1 1V20c0 .6-.4 1-1 1A17 17 0 0 1 3 4c0-.6.4-1 1-1h3.5c.6 0 1 .4 1 1 0 1.3.2 2.5.6 3.6.1.3 0 .7-.2 1z"/></svg>
        0471 592 304
      </li>
      <li>
        <svg viewBox="0 0 24 24" aria-hidden="true"><path d="M3 5h18v2l-9 6-9-6zm0 4.4l9 6 9-6V19H3z"/></svg>
        Brent.malvoy@quendix.com.au
      </li>
    </ul>

    <address class="address">87 Harrowgate Ave<br>Pindarra, QLD, 4000</address>

    <svg class="footer-bands" viewBox="0 0 745 50" aria-hidden="true">
      <polygon points="0,11 476,11 466,23 0,23" fill="var(--accent-blue)"/>
      <polygon points="498,0 745,0 745,50 0,50 0,29 474,29" fill="var(--brand-blue)"/>
    </svg>
    <div class="website">www.quendix.com.au</div>
  </section>
</body>
</html>
```